draft # 94 and #95- Could we see the accent pink line in more of a brush stroke and could you make the logo a little bigger and the name and title smaller. Please add the website on the front of the card and add "Locally owned and operated" in the back.
draft #58
We would like to include our tag line of the front of the card "Sweet moments, one swirl at a time!" Could we see this tagline in the same script font used in the logo. Could you also add
"Serving Riverton & Nearby Towns" on the back of the card, above the watermark
Mossworks-Could we see the coordinating stationery and envelopes for draft #58
Thank you all for your submissions! We are off to a good start. Please show us more options using the chocolate brown as the primary color and using pink as the accent color. Also please remember to include "Locally owned and operated." on the back of the card. (without quotation marks, of course)
We would also like to see the fountain part of the logo or the initials as a watermark on the back of the card.
We want to make sure the font on the logo is bigger than the other font size used on the rest of the card.
Draft # 54 could we see the front logo a little bigger and add Locally owned and operated on the back.
Thanks!=)

```html
<!DOCTYPE html>
<html lang="en">
<head>
<meta charset="utf-8">
<title>Dahlia Dips – Stationery Set</title>
<link href="https://fonts.googleapis.com/css2?family=Alex+Brush&family=Lora:wght@400;700&family=Open+Sans:wght@400;600&display=swap" rel="stylesheet">
<style>
  :root{
    --chocolate:#4a1a22;
    --chocolate-deep:#3a141b;
    --pink:#c8336b;
    --pink-soft:#e27aa0;
    --paper:#ffffff;
    --ink:#5a4a4a;
    --backdrop:#5b3a28;
  }
  *{margin:0;padding:0;box-sizing:border-box}
  html,body{width:1200px;height:897px;overflow:hidden}
  body{background:var(--backdrop);position:relative;font-family:"Open Sans",Arial,sans-serif;color:var(--ink)}

  .brand{display:flex;align-items:center;gap:6px;background:var(--paper);border:2px solid var(--chocolate);padding:6px 10px}
  .brand-dot{width:10px;height:10px;border-radius:50%;background:var(--pink);flex:none}
  .brand-name{font-family:"Lora",Georgia,serif;font-weight:700;color:var(--chocolate);font-size:16px;white-space:nowrap}
  .tagline{font-family:"Alex Brush",cursive;color:var(--paper);white-space:nowrap}
  .brush{position:absolute;left:0;width:100%}

  /* Letterhead */
  .letterhead{position:absolute;left:133px;top:29px;width:303px;height:620px;background:var(--paper);overflow:hidden}
  .letterhead .brand{position:absolute;left:16px;top:22px;padding:5px 8px}
  .letterhead .brand-name{font-size:14px}
  .letterhead .contact{position:absolute;left:170px;top:24px;font-size:7px;line-height:10px;color:var(--chocolate)}
  .letter-body{position:absolute;left:18px;top:88px;width:266px;font-size:5.2px;line-height:7.6px;color:var(--ink)}
  .letter-body p{margin-bottom:7px}
  .letter-body .address{margin-bottom:10px}
  .letterhead .footer-band{position:absolute;left:0;bottom:0;width:100%;height:100px}
  .letterhead .tagline{position:absolute;left:16px;bottom:20px;font-size:19px}

  /* Business card front */
  .card-front{position:absolute;left:618px;top:109px;width:388px;height:243px;background:var(--chocolate);overflow:hidden}
  .card-front .panel{position:absolute;left:0;top:0;width:200px;height:100%}
  .card-front .brand{position:absolute;left:22px;top:56px;padding:10px 12px}
  .card-front .brand-name{font-size:22px}
  .card-front .holder{position:absolute;left:214px;top:38px;color:var(--paper)}
  .holder-name{font-family:"Lora",Georgia,serif;font-weight:700;font-size:12px;margin-bottom:8px}
  .holder-line{font-size:7px;line-height:11px;display:flex;align-items:center;gap:4px}
  .holder-line i{width:4px;height:4px;border-radius:50%;background:var(--pink);display:inline-block}
  .card-front .tagline{position:absolute;right:20px;bottom:40px;font-size:20px}

  /* Business card back */
  .card-back{position:absolute;left:618px;top:364px;width:388px;height:218px;background:var(--chocolate);overflow:hidden}
  .card-back .service{position:absolute;top:26px;width:100%;text-align:center;font-family:"Lora",Georgia,serif;color:var(--pink-soft);font-size:13px}
  .card-back .watermark{position:absolute;top:84px;width:100%;text-align:center;font-family:"Lora",Georgia,serif;font-weight:700;font-size:34px;color:var(--chocolate-deep)}
  .card-back .local{position:absolute;top:158px;width:100%;text-align:center;font-family:"Alex Brush",cursive;font-size:14px;color:var(--pink-soft)}

  /* Envelopes */
  .envelope-small{position:absolute;left:133px;top:686px;width:412px;height:175px;background:var(--paper);overflow:hidden}
  .envelope-small .brand{position:absolute;left:14px;top:14px;padding:5px 9px}
  .envelope-small .brand-name{font-size:14px}
  .envelope-small .tagline{position:absolute;left:14px;bottom:10px;font-size:17px}
  .envelope-wide{position:absolute;left:582px;top:686px;width:424px;height:175px;background:var(--paper);overflow:hidden}
  .envelope-wide .flap{position:absolute;left:0;top:0;width:100%;height:100%}
  .seal{position:absolute;left:197px;top:70px;width:30px;height:30px;border-radius:50%;background:var(--pink);box-shadow:inset 0 0 0 3px #a8264f}
</style>
</head>
<body>

<section class="letterhead">
  <div class="brand"><span class="brand-dot"></span><span class="brand-name">Dahlia Dips</span></div>
  <div class="contact">
    <div>Ph: 555-201-4836</div>
    <div>F: 555-201-4837</div>
    <div>E: marisol@dahliadips.com</div>
  </div>
  <div class="letter-body">
    <p class="address">Adriana Solis<br>418 Orchard Lane<br>Riverton, Oregon</p>
    <p>Dear Adriana Solis,</p>
    <p>Thank you for choosing us for your upcoming celebration. We are delighted to share our menu of chocolate dipped fruit, pretzels and treats, each prepared fresh on the day of your event with care and attention to every detail.</p>
    <p>Our fountains arrive set up and ready to flow, with a friendly attendant to keep everything neat. Guests can choose from milk, dark or white chocolate and a colorful table of dippers.</p>
    <p>Please review the enclosed quote and let us know of any changes to your guest count, date or location. A small deposit holds your booking, and the balance is due one week before the event.</p>
    <p>We look forward to helping you make lasting memories with family and friends.</p>
    <p>Yours truly,<br><br>Marisol Vega</p>
  </div>
  <svg class="footer-band" viewBox="0 0 303 100" preserveAspectRatio="none" aria-hidden="true">
    <path d="M0 34 C80 18 200 48 303 12 L303 100 L0 100 Z" fill="var(--chocolate)"/>
    <path d="M0 30 C85 12 200 42 303 6 L303 14 C200 52 85 22 0 40 Z" fill="var(--pink)"/>
  </svg>
  <div class="tagline">Sweet moments, one swirl at a time!</div>
</section>

<section class="card-front">
  <svg class="panel" viewBox="0 0 200 243" preserveAspectRatio="none" aria-hidden="true">
    <path d="M0 0 L175 0 C210 70 205 150 165 243 L0 243 Z" fill="var(--paper)"/>
  </svg>
  <svg class="brush" style="bottom:0;height:90px" viewBox="0 0 388 90" preserveAspectRatio="none" aria-hidden="true">
    <path d="M0 34 C120 8 260 52 388 16 L388 90 L0 90 Z" fill="var(--chocolate)"/>
    <path d="M0 30 C125 2 260 46 388 10 L388 17 C260 58 125 16 0 42 Z" fill="var(--pink)"/>
  </svg>
  <div class="brand"><span class="brand-dot"></span><span class="brand-name">Dahlia Dips</span></div>
  <div class="holder">
    <div class="holder-name">Marisol Vega</div>
    <div class="holder-line"><i></i>555-201-4836</div>
    <div class="holder-line"><i></i>555-201-4837</div>
    <div class="holder-line"><i></i>marisol@dahliadips.com</div>
    <div class="holder-line"><i></i>www.dahliadips.com</div>
  </div>
  <div class="tagline">Sweet moments, one swirl at a time!</div>
</section>

<section class="card-back">
  <svg class="brush" style="bottom:0;height:40px" viewBox="0 0 388 40" preserveAspectRatio="none" aria-hidden="true">
    <path d="M0 22 C100 6 170 30 250 16 C310 6 350 20 388 12 L388 17 C350 26 310 12 250 22 C170 36 100 12 0 28 Z" fill="var(--pink)"/>
  </svg>
  <div class="service">Serving Riverton &amp; Nearby Towns</div>
  <div class="watermark">Dahlia Dips</div>
  <div class="local">Locally owned and operated</div>
</section>

<section class="envelope-small">
  <div class="brand"><span class="brand-dot"></span><span class="brand-name">Dahlia Dips</span></div>
  <svg class="brush" style="bottom:0;height:60px" viewBox="0 0 412 60" preserveAspectRatio="none" aria-hidden="true">
    <path d="M0 18 C120 4 280 28 412 6 L412 60 L0 60 Z" fill="var(--chocolate)"/>
    <path d="M0 14 C125 0 280 22 412 2 L412 7 C280 30 125 8 0 22 Z" fill="var(--pink)"/>
  </svg>
  <div class="tagline">Sweet moments, one swirl at a time!</div>
</section>

<section class="envelope-wide">
  <svg class="flap" viewBox="0 0 424 175" preserveAspectRatio="none" aria-hidden="true">
    <path d="M0 0 L424 0 L424 24 L250 84 C230 92 194 92 174 84 L0 24 Z" fill="var(--chocolate)"/>
  </svg>
  <div class="seal"></div>
</section>

</body>
</html>
```